Design a BOLD Ad Design for Fitness Club

We are fitness facility that is about to run our new "Bright Parent Reboot" program and we need a bold design created for an ad that will run on Instagram and Facebook.

The ad needs to be eye catching, easy to read and attractive so that someone stops scrolling and clicks to join.

The add needs to be sized to 1080 x 1080, include our logo and the text "Bright Parent Reboot" and "Starting September 23rd"

I have included an example photo, which is to be used as an example only of a design style that stands out to us, (colors, female photo style, etc)

I have also included our logo, which the yellow color can be changed for this design.

Thank you and we look forward to seeing your design.

```html
<!DOCTYPE html>
<html lang="en">
<head>
<meta charset="utf-8">
<title>Kinetra — Bright Parent Reboot ad set</title>
<link rel="stylesheet" href="https://fonts.googleapis.com/css2?family=Oswald:wght@200;700&family=Montserrat:wght@700;800&family=Mrs+Saint+Delafield&display=swap">
<style>
  :root {
    --pink: #ee14b8;
    --pink-soft: #d93a9f;
    --ink: #0a0a0a;
    --charcoal: #232323;
    --navy: #0d1030;
    --midnight: #121328;
    --plum: #3b2b4c;
    --gold: #e5b43c;
    --white: #ffffff;
    --page: #ffffff;
  }
  html, body {
    margin: 0;
    padding: 0;
    width: 1200px;
    height: 1200px;
    overflow: hidden;
    background: var(--page);
  }
  .ad-board {
    position: relative;
    width: 1200px;
    height: 1200px;
  }
  .ad-card {
    position: absolute;
    width: 498px;
    height: 498px;
    box-shadow: 0 14px 26px rgba(0,0,0,0.28);
    overflow: hidden;
  }
  .ad-card svg { display: block; width: 100%; height: 100%; }
  .card-a { left: 77px; top: 53px; }
  .card-b { left: 626px; top: 53px; }
  .card-c { left: 77px; top: 600px; }
  .card-d { left: 626px; top: 600px; }

  .brand-name { font-family: "Oswald", sans-serif; font-weight: 700; fill: var(--white); }
  .brand-tagline { font-family: "Montserrat", sans-serif; font-weight: 800; fill: var(--pink); letter-spacing: 3px; }
  .headline { font-family: "Oswald", sans-serif; font-weight: 700; }
  .headline-thin { font-family: "Oswald", sans-serif; font-weight: 200; fill: var(--white); }
  .headline-script { font-family: "Mrs Saint Delafield", cursive; fill: var(--pink); }
  .date-band-text { font-family: "Oswald", sans-serif; font-weight: 700; fill: var(--white); }
  .date-number { font-family: "Oswald", sans-serif; font-weight: 700; fill: var(--white); }
  .date-detail { font-family: "Montserrat", sans-serif; font-weight: 800; }
  .fill-white { fill: var(--white); }
  .fill-ink { fill: var(--ink); }
  .fill-pink { fill: var(--pink); }
</style>
</head>
<body>
<main class="ad-board">

  <!-- Variant A: charcoal with white torn base -->
  <section class="ad-card card-a">
    <svg viewBox="0 0 802 802" xmlns="http://www.w3.org/2000/svg">
      <defs>
        <linearGradient id="skinA" x1="0" y1="0" x2="0" y2="1">
          <stop offset="0" stop-color="#8a5634"/>
          <stop offset="1" stop-color="#3a2418"/>
        </linearGradient>
      </defs>
      <rect width="802" height="802" fill="var(--charcoal)"/>
      <path d="M90 560 A335 335 0 0 1 760 560 Z" fill="var(--pink)"/>
      <rect class="photo-slot" x="20" y="120" width="720" height="520" rx="40" fill="url(#skinA)" opacity="0.9" role="img" aria-label="Photo: smiling athletic woman in a black sports top flexing both arms"/>
      <path d="M0 520 L30 505 60 512 95 492 130 500 170 490 210 498 260 488 300 497 360 486 420 494 480 484 530 495 590 486 640 492 700 478 740 488 770 470 802 476 L802 802 L0 802 Z" fill="var(--white)"/>
      <text class="brand-name" x="410" y="180" font-size="96" text-anchor="middle">Kinetra</text>
      <text class="brand-tagline" x="410" y="118" font-size="11" text-anchor="middle" transform="translate(0 0)" dy="0" display="none"></text>
      <text class="brand-tagline" x="410" y="205" font-size="12" text-anchor="middle">PERSONAL GROUP TRAINING</text>
      <text class="headline fill-ink" x="125" y="643" font-size="112" textLength="550" lengthAdjust="spacingAndGlyphs">BRIGHT PARENT</text>
      <text class="headline-script" x="500" y="705" font-size="120" text-anchor="middle">Reboot</text>
      <rect x="130" y="726" width="543" height="44" fill="var(--pink)"/>
      <text class="date-band-text" x="401" y="765" font-size="44" text-anchor="middle">STARTING SEPTEMBER 23<tspan font-size="24" dy="-16">RD</tspan></text>
    </svg>
  </section>

  <!-- Variant B: navy with pink torn corners -->
  <section class="ad-card card-b">
    <svg viewBox="0 0 802 802" xmlns="http://www.w3.org/2000/svg">
      <defs>
        <linearGradient id="skinB" x1="0" y1="0" x2="0" y2="1">
          <stop offset="0" stop-color="#8a5634"/>
          <stop offset="1" stop-color="#1c1a2c"/>
        </linearGradient>
      </defs>
      <rect width="802" height="802" fill="var(--navy)"/>
      <path d="M0 0 L120 0 L108 30 96 40 88 80 70 110 62 150 44 180 36 230 22 270 14 320 4 350 0 345 Z" fill="var(--pink)"/>
      <rect class="photo-slot" x="15" y="120" width="725" height="420" rx="40" fill="url(#skinB)" role="img" aria-label="Photo: smiling athletic woman in a black sports top flexing both arms"/>
      <path d="M802 690 L775 700 750 712 725 716 700 735 670 742 650 758 610 768 585 780 540 786 515 798 500 802 L802 802 Z" fill="var(--pink)"/>
      <text class="brand-name" x="402" y="180" font-size="96" text-anchor="middle">Kinetra</text>
      <text class="brand-tagline" x="402" y="205" font-size="12" text-anchor="middle">PERSONAL GROUP TRAINING</text>
      <text class="headline fill-white" x="125" y="615" font-size="112" textLength="550" lengthAdjust="spacingAndGlyphs">BRIGHT PARENT</text>
      <text class="headline-script" x="410" y="680" font-size="120" text-anchor="middle">Reboot</text>
      <rect x="130" y="703" width="543" height="44" fill="var(--pink)"/>
      <text class="date-band-text" x="401" y="742" font-size="44" text-anchor="middle">STARTING SEPTEMBER 23<tspan font-size="24" dy="-16">RD</tspan></text>
    </svg>
  </section>

  <!-- Variant C: plum with stacked headline -->
  <section class="ad-card card-c">
    <svg viewBox="0 0 802 802" xmlns="http://www.w3.org/2000/svg">
      <defs>
        <linearGradient id="plumBg" x1="0" y1="0" x2="1" y2="1">
          <stop offset="0" stop-color="#2c2140"/>
          <stop offset="1" stop-color="#4a3550"/>
        </linearGradient>
        <linearGradient id="skinC" x1="0" y1="0" x2="1" y2="0">
          <stop offset="0" stop-color="#5a3422"/>
          <stop offset="1" stop-color="#3b2b4c" stop-opacity="0.2"/>
        </linearGradient>
      </defs>
      <rect width="802" height="802" fill="url(#plumBg)"/>
      <rect class="photo-slot" x="0" y="0" width="470" height="660" fill="url(#skinC)" role="img" aria-label="Photo: smiling woman with braided hair and earphones flexing one arm"/>
      <path d="M0 540 L40 545 80 560 130 566 170 590 220 600 260 622 300 640 360 660 420 690 470 700 520 720 580 735 640 752 700 762 760 770 802 776 L802 802 L0 802 Z" fill="var(--pink-soft)"/>
      <text class="brand-name" x="735" y="125" font-size="84" text-anchor="end">Kinetra</text>
      <text class="brand-tagline" x="705" y="152" font-size="11" text-anchor="end">PERSONAL GROUP TRAINING</text>
      <text class="headline fill-white" x="425" y="380" font-size="160" textLength="312" lengthAdjust="spacingAndGlyphs">BRIGHT</text>
      <text class="headline fill-white" x="420" y="470" font-size="112" textLength="325" lengthAdjust="spacingAndGlyphs">PARENT</text>
      <text class="headline-script" x="600" y="530" font-size="110" text-anchor="middle">Reboot</text>
      <text class="date-number" x="420" y="678" font-size="92">23</text>
      <rect x="522" y="595" width="4" height="88" fill="var(--gold)"/>
      <text class="date-detail fill-white" x="545" y="618" font-size="28">MONDAY</text>
      <text class="date-detail fill-pink" x="545" y="650" font-size="28">SEPTEMBER</text>
      <text class="date-detail fill-white" x="545" y="682" font-size="28">10AM</text>
    </svg>
  </section>

  <!-- Variant D: midnight with right-side figure -->
  <section class="ad-card card-d">
    <svg viewBox="0 0 802 802" xmlns="http://www.w3.org/2000/svg">
      <defs>
        <linearGradient id="nightBg" x1="0" y1="0" x2="1" y2="1">
          <stop offset="0" stop-color="var(--midnight)"/>
          <stop offset="0.55" stop-color="#2a1d3a"/>
          <stop offset="1" stop-color="#7a3470"/>
        </linearGradient>
        <linearGradient id="skinD" x1="0" y1="0" x2="0" y2="1">
          <stop offset="0" stop-color="#6a3e2e"/>
          <stop offset="1" stop-color="#a36a4a"/>
        </linearGradient>
      </defs>
      <rect width="802" height="802" fill="url(#nightBg)"/>
      <rect class="photo-slot" x="390" y="10" width="380" height="690" rx="60" fill="url(#skinD)" opacity="0.85" role="img" aria-label="Photo: muscular woman in a white top and purple shorts holding a dumbbell"/>
      <path d="M802 580 L770 590 740 600 720 625 680 640 650 660 600 672 560 690 520 708 470 725 420 742 370 760 300 780 240 800 220 802 L802 802 Z" fill="var(--pink-soft)"/>
      <text class="brand-name" x="75" y="128" font-size="84">Kinetra</text>
      <text class="brand-tagline" x="108" y="150" font-size="11">PERSONAL GROUP TRAINING</text>
      <text class="headline-thin" x="75" y="392" font-size="200" textLength="325" lengthAdjust="spacingAndGlyphs">BRIGHT</text>
      <text class="headline fill-white" x="75" y="490" font-size="118" textLength="325" lengthAdjust="spacingAndGlyphs">PARENT</text>
      <text class="headline-script" x="240" y="555" font-size="110" text-anchor="middle">Reboot</text>
      <rect x="75" y="615" width="82" height="100" fill="var(--pink)"/>
      <text class="date-number" x="116" y="698" font-size="72" text-anchor="middle">23</text>
      <text class="date-detail fill-pink" x="170" y="640" font-size="20">STARTING</text>
      <text class="date-detail fill-pink" x="170" y="662" font-size="20">MONDAY</text>
      <text class="date-detail fill-white" x="170" y="684" font-size="20">SEPTEMBER</text>
      <text class="date-detail fill-white" x="170" y="706" font-size="20">10AM</text>
    </svg>
  </section>

</main>
</body>
</html>
```